Pause Your Day And Browse- PYDAB poster

I am the Vice President of Advocacy for the Coastal School Bookkeepers Guild. I am looking to have a set of posters made for PYDAB (Pause Your Day and Browse) October 23. PYDAB is a time when all school children in BC are encouraged to Pause Your Day and Browse for 15-20 minutes at some point in their day.

I would like to get a set of 2 digital posters designed (if possible it would be nice to have the option to print to both 11 x 17 and 8.5 x 11 paper). We need a poster that is high school (Grade 8-12) appropriate and one that is elementary (Grade k-7) appropriate. Both posters need to be replicated in French. All posters need to have the PEWU logo on them as well as the Coastal School Bookkeepers Guild Logo.

Here is a link to last year's successful design http://pewu-sample.ca/csbg/info/outreach.html
There are two additional samples in the uploaded files section.

Each poster needs to have the following information:

-Pause Your Day and Browse (PYDAB)
- The date Monday, October 23, 2017
-the logo for the PEWU (attached)
-the logo for the CSBG (attached)- the logos do not have to be large.

Target Market(s)

Children ages 5-12 and 12-17 as well as their teachers

Industry/Entity Type

Teacher

Font styles to use
Sans Serif

Requirements
Must have
• Must have both logos- colours may be changed for either or both
Nice to have
• Clear, Bright lettering. Images of child or children enjoying reading
Should not have
• stereotypes

```html
<!DOCTYPE html>
<html lang="en">
<head>
<meta charset="utf-8">
<title>PYDAB – Pause Your Day and Browse poster</title>
<link rel="stylesheet" href="https://fonts.googleapis.com/css2?family=Roboto:wght@400;500&family=Roboto+Condensed:wght@500&display=swap">
<style>
  :root {
    --page-bg: #f3f3f3;
    --frame-grey: #4a4a4a;
    --paper: #fbfbfb;
    --headline-grey: #4b4b4b;
    --tan: #b48f78;
    --emblem-tint: #e8ddd2;
    --logo-green: #2f8a3e;
    --logo-dark: #1d1d1d;
    --photo-light: #ece7e4;
    --photo-mid: #c9b49a;
    --photo-deep: #8d7b93;
  }
  * { box-sizing: border-box; margin: 0; padding: 0; }
  html, body {
    width: 1200px;
    height: 1200px;
    overflow: hidden;
    background: var(--page-bg);
  }
  .poster {
    position: absolute;
    left: 50px;
    top: 208px;
    width: 1100px;
    height: 783px;
    background: var(--paper);
    border: 30px solid var(--frame-grey);
  }
  .reader-photo {
    position: absolute;
    left: 0;
    top: 40px;
    width: 480px;
    height: 683px;
    background:
      radial-gradient(ellipse 30% 38% at 60% 30%, var(--photo-deep) 0%, transparent 70%),
      linear-gradient(180deg, var(--photo-light) 0%, var(--photo-mid) 55%, #a88a72 100%);
    opacity: 0.9;
  }
  .partner-emblem {
    position: absolute;
    left: 692px;
    top: 132px;
    width: 136px;
    height: 136px;
    border-radius: 50%;
    border: 3px solid var(--emblem-tint);
    display: flex;
    align-items: center;
    justify-content: center;
    font-family: "Roboto", Arial, sans-serif;
    font-weight: 500;
    font-size: 34px;
    color: var(--emblem-tint);
  }
  .title-block {
    position: absolute;
    left: 500px;
    top: 318px;
    width: 520px;
    text-align: center;
  }
  .headline {
    font-family: "Roboto", Arial, sans-serif;
    font-weight: 500;
    font-size: 140px;
    line-height: 0.95;
    letter-spacing: -2px;
    color: var(--headline-grey);
  }
  .tagline {
    margin-top: 10px;
    font-family: "Roboto Condensed", "Arial Narrow", sans-serif;
    font-weight: 500;
    font-size: 34px;
    line-height: 1;
    color: var(--tan);
    white-space: nowrap;
  }
  .event-date {
    margin-top: 18px;
    font-family: "Roboto", Arial, sans-serif;
    font-weight: 500;
    font-size: 31px;
    line-height: 1;
    color: var(--tan);
    white-space: nowrap;
  }
  .guild-mark {
    position: absolute;
    right: 30px;
    bottom: 22px;
    display: flex;
    align-items: center;
    gap: 8px;
  }
  .guild-mark__square {
    width: 22px;
    height: 22px;
    background: var(--logo-green);
  }
  .guild-mark__name {
    font-family: "Roboto", Arial, sans-serif;
    font-weight: 500;
    font-size: 40px;
    line-height: 1;
    color: var(--logo-dark);
  }
</style>
</head>
<body>
  <main class="poster">
    <div class="reader-photo" role="img" aria-label="Photo of a young girl in a plaid shirt and jeans sitting on a stack of large books, reading a blue book"></div>

    <div class="partner-emblem">PEWU</div>

    <section class="title-block">
      <h1 class="headline">PYDAB</h1>
      <p class="tagline">PAUSE YOUR DAY AND BROWSE</p>
      <p class="event-date">MONDAY, OCTOBER 23, 2017</p>
    </section>

    <div class="guild-mark">
      <span class="guild-mark__square"></span>
      <span class="guild-mark__name">csbg</span>
    </div>
  </main>
</body>
</html>
```